Piano Decal Artwork

Every grand piano has on its soundboard a decal.
(You may google piano decal for examples).

The decal shoud incorporate our logo and the words: Lumen Vox Perpetua
Updates

Thank you for the submitting your creative design proposal. What we are missing is that our logo is not integrated into the design in or the words: Lumen Vox PerpetuaĀ  are missing.

You can find our logo at www.vorelta-keys.example.

Thanks.

Please note that we have provided the company's logo in the file section.

Target Market(s)

We produce high quality grand pianos in China. Our customer base is usually interested in Japanese product and the fact that our instruments are produced in China poses sometimes a hurdle- even though we lead the piano industry in service and warranty standards (see: www.vorelta-keys.example. Our customers are adults between 30 and 65 who are better educated and either seek a piano for themselves or for their children.

While our instruments are produced in the Far East, the engineering and design comes from master craftsmen from Austria and France.

Logo Text

Lumen Vox Perpetua

Requirements
Must have
• The decal should be simple and match our corporate identity. See: www.vorelta-keys.example

```html
<!DOCTYPE html>
<html lang="en">
<head>
<meta charset="utf-8">
<title>Lumen Vox Perpetua – Soundboard Decal</title>
<link rel="stylesheet" href="https://fonts.googleapis.com/css2?family=Saira+Extra+Condensed:wght@200;300&display=swap">
<style>
  :root {
    --page-bg: #ffffff;
    --decal-edge: #111010;
    --decal-fill: #3a3836;
    --decal-shade: #252221;
    --decal-sheen: #3b3836;
    --decal-text: #ffffff;
  }
  html, body {
    margin: 0;
    padding: 0;
    width: 1200px;
    height: 900px;
    overflow: hidden;
    background: var(--page-bg);
  }
  .decal-canvas {
    display: block;
    width: 1200px;
    height: 900px;
  }
  .decal-body { fill: var(--decal-fill); }
  .decal-shade { fill: var(--decal-shade); }
  .decal-sheen { fill: none; stroke: var(--decal-sheen); stroke-width: 3; }
  .decal-border { fill: none; stroke: var(--decal-edge); stroke-width: 3; }
  .decal-motto {
    fill: var(--decal-text);
    font-family: "Saira Extra Condensed", "Arial Narrow", sans-serif;
    font-weight: 200;
    font-size: 62px;
    text-anchor: middle;
  }
</style>
</head>
<body>
<svg class="decal-canvas" viewBox="0 0 1200 900" xmlns="http://www.w3.org/2000/svg" aria-label="Lumen Vox Perpetua piano decal">
  <defs>
    <clipPath id="decal-shape">
      <rect x="508" y="111" width="178" height="672" rx="18" ry="18"/>
    </clipPath>
  </defs>

  <g class="decal" clip-path="url(#decal-shape)">
    <rect class="decal-body" x="508" y="111" width="178" height="672"/>
    <path class="decal-shade" d="M500,560 C540,505 610,478 700,478 L700,790 L500,790 Z"/>
    <path class="decal-sheen" d="M650,776 C668,766 680,752 686,735"/>
  </g>
  <rect class="decal-border" x="508" y="111" width="178" height="672" rx="18" ry="18"/>

  <g class="decal-motto">
    <text x="597" y="617" textLength="96" lengthAdjust="spacingAndGlyphs">LUMEN</text>
    <text x="597" y="671" textLength="62" lengthAdjust="spacingAndGlyphs">VOX</text>
    <text x="597" y="727" textLength="146" lengthAdjust="spacingAndGlyphs">PERPETUA</text>
  </g>
</svg>
</body>
</html>
```